Global organization bringing life-changing education to refugee children needs website redesign

As NOVAworld continues to expand its programs, the website (novaworld.org) needs to reflect our growing impact.

This task includes:
- Enhancing/redesigning the current website in WIX
- Updating fonts and color scheme to match the tone we're trying to achieve (see below)
- Rely more heavily on images/photos on each page (photos attached - more are available)
- Match navigation/content to the attached copy deck

Priorities for website design are:
Homepage – Overview of our mission, our impact and media coverage to prove credibility. Add scrolling header images that feature our key programs and latest news.
Other pages – Improve and optimize design and user experience. Goal is to make the site more “skimmable” and easier to navigate.

The new website should be clean, sophisticated and inspiring with more prominence placed on partnerships. The site should inform users about our work and encourage them to support NOVAworld. Users should be able to easily and effortlessly navigate the site.

About NOVAworld:
NOVAworld provides high-quality education to the world’s most vulnerable children.

NOVAworld brings these learning experiences to children through an international constellation of “Nests” – innovative and engaging education programs for young children and their families. In collaboration with partner organizations, NOVAworld establishes culturally-responsive, play-based early education programs in refugee camps, migrant shelters, and communities experiencing extreme hardship.

Communication Objective(s):
- NOVAworld is leading the way in providing high-quality early childhood education to the world’s most vulnerable children
- NOVAworld is making a measurable impact on children and families
- NOVAworld’s work is acclaimed by reputable media sources, leaders and organizations

Tonality/look and feel:
Empowering, forward-thinking, inspiring, warm, bold, confident and clean

Target Market(s)

Prospective donors, partners and volunteers who are passionate about helping children

Industry/Entity Type

Non-profit, education

Coding

Coded - Design and coding required

Font styles to use
Sans Serif
Other font styles liked:
• Open to other suggestions

Requirements
Must have
• The new website should be clean, sophisticated and inspiring with more prominence placed on partnerships. The site should inform users about our work and encourage them to support NOVAworld. Users should be able to easily and effortlessly navigate the site. Include a call-to-action on every page.
Nice to have
• Larger, more prominent photos and more sophisticated fonts and colors.
Should not have
• Too many colors and copy

```html
<!DOCTYPE html>
<html lang="en">
<head>
<meta charset="utf-8">
<title>NOVAworld — Website Redesign</title>
<link href="https://fonts.googleapis.com/css2?family=Poppins:wght@300;400;500;600;700&display=swap" rel="stylesheet">
<style>
:root{
  --board:#d9d9d9;
  --gold:#c39c5e;
  --pill:#e6c65a;
  --navy:#213a8a;
  --ink:#2e2e2e;
  --muted:#6b6b6b;
  --cream:#f4eee0;
  --white:#ffffff;
}
*{box-sizing:border-box;margin:0;padding:0}
html,body{width:1036px;height:1200px;overflow:hidden}
body{background:var(--board);font-family:"Poppins",sans-serif;color:var(--ink);position:relative}
.board-title{position:absolute;font-weight:700;color:#3a3a3a;letter-spacing:.2px;line-height:1}
.page{position:absolute;background:var(--white);overflow:hidden}
.abs{position:absolute}
.photo{position:absolute}
.shade{position:absolute;inset:0;background:rgba(20,20,30,.35)}
.nav{position:absolute;left:0;right:0;display:flex;align-items:center}
.logo{display:flex;align-items:center;gap:2px;color:var(--white);font-weight:600}
.logo-mark{width:9px;height:6px;background:var(--gold);border-radius:1px}
.nav-links{display:flex;color:var(--white);text-transform:uppercase;font-weight:500}
.nav-links span{white-space:nowrap}
.pill{display:inline-flex;align-items:center;justify-content:center;border-radius:20px;font-weight:500;white-space:nowrap}
.pill-gold{background:var(--pill);color:var(--ink)}
.pill-navy{background:var(--navy);color:var(--white)}
.hero-title{position:absolute;left:0;right:0;text-align:center;color:var(--white);font-weight:500;line-height:1.08}
.center{left:0;right:0;text-align:center}
.navy{color:var(--navy)}
.link{font-size:3.4px;color:var(--navy);font-weight:600}
.stat-num{color:var(--navy);font-weight:500;line-height:1.1}
.stat-label{color:var(--ink);line-height:1.35}
.card-box{position:absolute;background:rgba(195,156,94,.92);color:var(--white);padding:5px 6px}
.card-box .name{font-size:3.8px}
.card-box .place{font-size:2.8px;opacity:.85;margin-top:1px}
.card-box .more{position:absolute;bottom:5px;left:6px;font-size:2.8px}
.outline-box{position:absolute;border:.6px solid #e3e3e3;padding:5px 6px;background:var(--white)}
.outline-box .name{font-size:3.3px;line-height:1.4}
.outline-box .place{font-size:2.8px;color:var(--muted)}
.outline-box .more{position:absolute;bottom:5px;left:6px;font-size:2.8px;color:var(--navy)}
.field{position:absolute;border-bottom:.5px solid #9a9a9a;font-size:2.6px;color:var(--muted);padding-bottom:1px}
.addr{font-size:3px;line-height:1.55;color:var(--ink)}
.addr b{font-weight:600}
.badge{position:absolute;background:#dcdcdc;border-radius:1px}
.rule{position:absolute;height:.5px;background:#d8d8d8}
</style>
</head>
<body>

<h2 class="board-title" style="left:60px;top:34px;font-size:25px">Homepage</h2>
<h2 class="board-title" style="left:408px;top:43px;font-size:24px">Partner &amp; Funders</h2>

<!-- ===================== HOME ===================== -->
<section class="page" style="left:61px;top:82px;width:306px;height:1098px">

  <div class="photo" role="img" aria-label="Children drawing together at a classroom table" style="left:0;top:0;width:306px;height:168px;background:linear-gradient(120deg,#3b2c28 0%,#7a5a44 45%,#a88466 70%,#5e4434 100%)"></div>
  <div class="shade" style="height:168px;bottom:auto"></div>

  <nav class="nav" style="top:6px;padding:0 26px;height:12px">
    <div class="logo" style="font-size:8px"><span class="logo-mark"></span>NOVA</div>
    <div class="nav-links" style="font-size:2.9px;gap:6px;margin-left:20px">
      <span>Home</span><span>Who we are</span><span>Partners &amp; Funders</span><span>Our works</span><span>Get involved</span>
    </div>
    <span class="pill pill-gold" style="margin-left:auto;font-size:2.9px;width:31px;height:10px">DONATE</span>
  </nav>

  <h1 class="hero-title" style="top:63px;font-size:17px">Education is a<br>human right</h1>
  <div class="abs center" style="top:111px"><span class="pill pill-navy" style="font-size:3px;width:26px;height:8px">Read more</span></div>
  <svg class="abs" style="left:9px;top:76px" width="8" height="10" viewBox="0 0 8 10"><path d="M6 1 2 5l4 4" stroke="#fff" stroke-width="1" fill="none"/></svg>
  <svg class="abs" style="left:288px;top:76px" width="8" height="10" viewBox="0 0 8 10"><path d="M2 1l4 4-4 4" stroke="#fff" stroke-width="1" fill="none"/></svg>
  <svg class="abs" style="left:143px;top:145px" width="22" height="4" viewBox="0 0 22 4"><circle cx="2" cy="2" r="1.4" fill="#fff"/><circle cx="8" cy="2" r="1.2" fill="none" stroke="#fff" stroke-width=".5"/><circle cx="14" cy="2" r="1.2" fill="none" stroke="#fff" stroke-width=".5"/><circle cx="20" cy="2" r="1.2" fill="none" stroke="#fff" stroke-width=".5"/></svg>

  <svg class="abs" style="left:18px;top:197px" width="18" height="18" viewBox="0 0 18 18"><rect x="1" y="9" width="12" height="8" fill="#c39c5e"/><circle cx="12" cy="6" r="5" fill="#213a8a"/><path d="M12 3v3h2" stroke="#fff" stroke-width=".8" fill="none"/></svg>
  <div class="abs" style="left:44px;top:199px"><div class="stat-num" style="font-size:6.5px">100,000 +</div><div class="stat-label" style="font-size:3.6px">hours of education<br>provided to children</div></div>
  <svg class="abs" style="left:107px;top:196px" width="22" height="20" viewBox="0 0 22 20"><circle cx="7" cy="4" r="2.5" fill="#c39c5e"/><rect x="4.5" y="7" width="5" height="8" rx="1.5" fill="#c39c5e"/><circle cx="15" cy="7" r="2" fill="#213a8a"/><rect x="13" y="10" width="4" height="7" rx="1.2" fill="#213a8a"/><circle cx="2.5" cy="11" r="1.5" fill="#213a8a"/></svg>
  <div class="abs" style="left:134px;top:198px"><div class="stat-num" style="font-size:6.5px">Over 5,000</div><div class="stat-label" style="font-size:3.6px">children and families<br>enrolled</div></div>
  <svg class="abs" style="left:200px;top:196px" width="24" height="20" viewBox="0 0 24 20"><circle cx="5" cy="4" r="2.3" fill="#c39c5e"/><path d="M3 8h5v6H3zM2 14h10v2H2z" fill="#c39c5e"/><circle cx="17" cy="5" r="2" fill="#213a8a"/><path d="M14 9h6v7h-6z" fill="#213a8a"/></svg>
  <div class="abs" style="left:229px;top:198px"><div class="stat-num" style="font-size:6.5px">17 classrooms</div><div class="stat-label" style="font-size:3.6px">across 3 continents</div></div>

  <div class="abs" style="left:0;top:254px;width:306px;height:137px;background:var(--gold)"></div>
  <div class="photo" role="img" aria-label="Smiling children holding seedlings in plastic cups" style="left:18px;top:270px;width:111px;height:133px;background:linear-gradient(160deg,#7c6a55,#4a3a2e 55%,#a08a6c)"></div>
  <p class="abs" style="left:150px;top:268px;width:132px;font-size:6.6px;line-height:1.22;color:#fff;font-weight:400">NOVAworld provides innovative education for children and families impacted by displacement and poverty worldwide.</p>
  <p class="abs" style="left:148px;top:312px;width:140px;font-size:3.5px;line-height:1.65;color:#fff">NOVAworld brings high-quality learning experiences to under-served communities around the world through an international constellation of "Havens" – innovative and engaging education programs for young children. In collaboration with partner organizations, NOVAworld establishes culturally-responsive, play-based early education programs in refugee camps, migrant shelters, and communities experiencing extreme hardship.</p>
  <div class="abs" style="left:148px;top:376px;font-size:3.4px;color:#fff">Read more →</div>

  <h3 class="abs center" style="top:426px;font-size:7.2px;font-weight:500">Latest News &amp; Programs</h3>
  <div class="photo" role="img" aria-label="Child standing at a classroom whiteboard" style="left:21px;top:449px;width:78px;height:59px;background:linear-gradient(140deg,#d9d3c4,#8e8a80)"></div>
  <div class="photo" role="img" aria-label="Students painting a large world map mural" style="left:111px;top:449px;width:78px;height:59px;background:linear-gradient(140deg,#c9c7c0,#a86f62 50%,#6f88b0)"></div>
  <div class="photo" role="img" aria-label="Children playing in a school courtyard" style="left:202px;top:449px;width:78px;height:59px;background:linear-gradient(140deg,#7d6a58,#b39a7c 55%,#5b6a55)"></div>

  <div class="abs" style="left:21px;top:516px;width:80px"><div style="font-size:3px">April 2022 Bayline Public Radio</div><div style="font-size:4.1px;line-height:1.35;margin-top:3px">For Migrants Stuck in Tijuana, This School Offers a Place to Grow and Dream</div></div>
  <div class="abs" style="left:111px;top:516px;width:80px"><div style="font-size:3px">June 2022, Ardent &amp; Vale Gallery</div><div style="font-size:4.1px;line-height:1.35;margin-top:3px">Ardent &amp; Vale Launches Education Project in Los Angeles</div></div>
  <div class="abs" style="left:202px;top:516px;width:80px"><div style="font-size:3px">May 2021 Harbor City Tribune</div><div style="font-size:4.1px;line-height:1.35;margin-top:3px">Canyon Haven School Offers Respite from Chaos of Migrant Life for Expelled Children in Tijuana</div></div>
  <div class="abs link" style="left:21px;top:556px">Read more →</div>
  <div class="abs link" style="left:111px;top:556px">Read more →</div>
  <div class="abs link" style="left:202px;top:556px">Read more →</div>
  <div class="abs center" style="top:582px"><span class="pill pill-gold" style="font-size:3px;width:51px;height:12px">More our newsroom</span></div>

  <div class="photo" role="img" aria-label="Hands of children working together on an activity, tinted blue" style="left:0;top:611px;width:306px;height:119px;background:linear-gradient(120deg,#2c4a86,#3f5f9c 50%,#2a4478)"></div>
  <p class="abs center" style="top:633px;padding:0 60px;font-size:7.4px;line-height:1.55;color:#fff">"NOVAworld is dedicated to giving children in refugee camps a safe place to learn and play… I'm thankful for the people at NOVAworld who are doing this life-changing work."</p>
  <div class="abs center" style="top:683px;font-size:6px;color:#fff">— CONGRESSWOMAN DANA WHITFIELD</div>
  <div class="abs center" style="top:701px"><span class="pill pill-gold" style="font-size:3px;width:31px;height:9px">Read more</span></div>

  <div class="photo" role="img" aria-label="Faded photo of a child in a classroom" style="left:0;top:730px;width:306px;height:132px;background:linear-gradient(120deg,#f6f1ea,#ede3d4 50%,#f3ece2)"></div>
  <h3 class="abs center" style="top:740px;font-size:7.4px;font-weight:500">Haven Schools</h3>
  <div class="card-box" style="left:40px;top:758px;width:72px;height:40px"><div class="name">Canyon Haven</div><div class="place">Canyon Haven</div><div class="more">Read more &nbsp;&nbsp;&nbsp;&nbsp;&nbsp;&nbsp;→</div></div>
  <div class="card-box" style="left:119px;top:758px;width:72px;height:40px"><div class="name">Haven Norte</div><div class="place">Haven Athens</div><div class="more">Read more &nbsp;&nbsp;&nbsp;&nbsp;→</div></div>
  <div class="card-box" style="left:195px;top:758px;width:72px;height:40px"><div class="name">Haven Congo</div><div class="place">Mumosho, Dr Congo</div><div class="more">Read more &nbsp;&nbsp;&nbsp;&nbsp;→</div></div>
  <div class="card-box" style="left:81px;top:808px;width:72px;height:40px"><div class="name">Haven Zimbabwe</div><div class="place">Harare, Zimbabwe</div><div class="more">Read more &nbsp;&nbsp;&nbsp;&nbsp;→</div></div>
  <div class="card-box" style="left:155px;top:808px;width:72px;height:40px"><div class="name">Haven Athens</div><div class="place">Athens, Greece</div><div class="more">Read more &nbsp;&nbsp;&nbsp;&nbsp;→</div></div>

  <h3 class="abs" style="left:25px;top:872px;font-size:6.6px;font-weight:500">Parenting Programs</h3>
  <h3 class="abs" style="left:200px;top:872px;font-size:6.6px;font-weight:500">Parent &amp; Me Program</h3>
  <div class="outline-box" style="left:25px;top:891px;width:72px;height:40px"><div class="name">Tijuana Parenting<br>Program</div><div class="place">Tijuana, Mexico</div><div class="more">Read more &nbsp;&nbsp;&nbsp;&nbsp;&nbsp;→</div></div>
  <div class="outline-box" style="left:104px;top:891px;width:72px;height:40px"><div class="name">Los Angeles<br>Parenting Program</div><div class="place">Los Angeles, CA</div><div class="more">Read more &nbsp;&nbsp;&nbsp;&nbsp;&nbsp;→</div></div>
  <div class="outline-box" style="left:199px;top:891px;width:72px;height:40px"><div class="name">Los Angeles<br>Parenting Program</div><div class="place">Los Angeles, CA</div><div class="more">Read more &nbsp;&nbsp;&nbsp;&nbsp;&nbsp;→</div></div>

  <div class="photo" role="img" aria-label="Smiling child in soft dark light" style="left:0;top:950px;width:306px;height:74px;background:linear-gradient(110deg,#2a2b33,#4a4a52 55%,#2b2d35)"></div>
  <h3 class="abs center" style="top:966px;font-size:8px;font-weight:400;color:#fff">Take Action</h3>
  <div class="abs center" style="top:990px;display:flex;justify-content:center;gap:6px">
    <span class="pill pill-gold" style="font-size:3px;width:45px;height:14px">♡ Donate</span>
    <span class="pill pill-navy" style="font-size:3px;width:45px;height:14px">Partner with us</span>
    <span class="pill pill-navy" style="font-size:3px;width:45px;height:14px">Volunteer with us</span>
  </div>

  <h4 class="abs" style="left:22px;top:1045px;font-size:6.4px;font-weight:500">Sign up for email</h4>
  <div class="field" style="left:22px;top:1060px;width:48px">First name</div>
  <div class="field" style="left:74px;top:1060px;width:48px">Last name</div>
  <div class="field" style="left:22px;top:1072px;width:100px">Email address</div>
  <span class="abs pill pill-gold" style="left:22px;top:1087px;font-size:3px;width:29px;height:10px">Submit</span>
  <div class="abs addr" style="left:149px;top:1047px"><b>NOVAworld</b><br>412 Linden Crest, Suite 18<br>Harbor View, California 90000<br>+1 555.010.4421<br>info@novaworld.org<br>EIN# 00-0000000</div>
</section>

<!-- ===================== PARTNERS ===================== -->
<section class="page" style="left:410px;top:82px;width:245px;height:1105px">
  <div class="photo" role="img" aria-label="Students painting a colorful wall mural on ladders" style="left:0;top:0;width:245px;height:121px;background:linear-gradient(130deg,#d8cfc0,#b49a86 45%,#8f8580)"></div>
  <div class="shade" style="height:121px;bottom:auto;background:rgba(20,20,30,.25)"></div>
  <nav class="nav" style="top:4px;padding:0 20px;height:10px">
    <div class="logo" style="font-size:6px"><span class="logo-mark" style="width:7px;height:5px"></span>NOVA</div>
    <div class="nav-links" style="font-size:2.3px;gap:5px;margin-left:18px">
      <span>Home</span><span>Who we are</span><span>Partners &amp; Funders</span><span>Our works</span><span>Get involved</span>
    </div>
    <span class="pill pill-gold" style="margin-left:auto;font-size:2.3px;width:25px;height:8px">DONATE</span>
  </nav>
  <h1 class="hero-title" style="top:46px;font-size:14px">Partners &amp; Funders</h1>

  <div class="abs" style="left:0;top:121px;width:245px;height:110px;background:var(--cream)"></div>
  <div class="photo" role="img" aria-label="Group photo of students and artists in a gallery" style="left:15px;top:129px;width:213px;height:89px;background:linear-gradient(120deg,#4b3f38,#7a6654 50%,#3f3630)"></div>
  <div class="abs" style="left:15px;top:163px;width:213px;text-align:center;color:#fff;font-size:6px">Partnership with Ardent + Vale</div>
  <div class="abs" style="left:15px;top:172px;width:213px;text-align:center;color:#fff;font-size:2.8px">Read more →</div>
  <svg class="abs" style="left:24px;top:168px" width="6" height="8" viewBox="0 0 6 8"><path d="M5 1 1 4l4 3" stroke="#fff" stroke-width=".8" fill="none"/></svg>
  <svg class="abs" style="left:213px;top:168px" width="6" height="8" viewBox="0 0 6 8"><path d="M1 1l4 3-4 3" stroke="#fff" stroke-width=".8" fill="none"/></svg>

  <div class="photo" role="img" aria-label="Teacher and children tending a garden" style="left:15px;top:240px;width:95px;height:88px;background:linear-gradient(150deg,#6f7c4f,#c9a24a 50%,#4f5c3a)"></div>
  <div class="abs" style="left:120px;top:247px;width:108px;font-size:2.8px;line-height:1.55">
    <p>NOVAworld recognizes that partnership and collaboration are crucial for the success of any humanitarian endeavor, and we are honored to partner with local NGOs and organizations worldwide.</p>
    <p style="margin-top:4px">Our partners provide on-the-ground support, local knowledge and valuable resources that allow us to implement education and parenting programs in areas of the world that need them most.</p>
    <p style="margin-top:4px">NOVAworld is also generously supported by a community of private donors and foundations. Their contributions have allowed us to help disadvantaged children and their families heal and thrive through high-quality early childhood and parenting programs around the globe.</p>
  </div>

  <h3 class="abs center navy" style="top:351px;font-size:5.5px;font-weight:500">Thank you to our partners &amp; supporters</h3>
  <div class="badge" style="left:36px;top:370px;width:20px;height:17px"></div>
  <div class="badge" style="left:62px;top:370px;width:20px;height:17px"></div>
  <div class="badge" style="left:90px;top:372px;width:28px;height:13px"></div>
  <div class="badge" style="left:129px;top:373px;width:40px;height:10px"></div>
  <div class="badge" style="left:178px;top:370px;width:28px;height:16px"></div>
  <div class="badge" style="left:36px;top:402px;width:20px;height:18px"></div>
  <div class="badge" style="left:66px;top:404px;width:30px;height:14px"></div>
  <div class="badge" style="left:108px;top:404px;width:16px;height:15px"></div>
  <div class="badge" style="left:129px;top:408px;width:54px;height:6px"></div>
  <div class="badge" style="left:189px;top:402px;width:20px;height:18px"></div>
  <div class="badge" style="left:36px;top:431px;width:50px;height:7px"></div>
  <div class="badge" style="left:100px;top:428px;width:16px;height:13px"></div>
  <div class="badge" style="left:124px;top:428px;width:40px;height:13px"></div>
  <div class="badge" style="left:176px;top:430px;width:32px;height:9px"></div>
  <div class="badge" style="left:36px;top:454px;width:32px;height:8px"></div>
  <div class="badge" style="left:83px;top:450px;width:30px;height:14px"></div>
  <div class="badge" style="left:127px;top:454px;width:38px;height:7px"></div>
  <div class="badge" style="left:180px;top:451px;width:30px;height:11px"></div>
  <div class="badge" style="left:36px;top:474px;width:28px;height:10px"></div>
  <div class="badge" style="left:84px;top:472px;width:28px;height:12px"></div>
  <div class="badge" style="left:124px;top:474px;width:34px;height:9px"></div>
  <div class="badge" style="left:172px;top:474px;width:42px;height:9px"></div>

  <div class="abs" style="left:0;top:509px;width:245px;height:28px;background:var(--cream)"></div>
  <h3 class="abs center" style="top:519px;font-size:5.6px;font-weight:500">Key Partnerships</h3>
  <div class="photo" role="img" aria-label="Artist with a group of high school students in a gallery" style="left:0;top:537px;width:245px;height:70px;background:linear-gradient(120deg,#3b3430,#6c5a4b 50%,#3a322d)"></div>
  <div class="abs center" style="top:564px;color:#fff;font-size:5.6px">Theo Marlow and Ardent &amp; Vale Gallery</div>
  <div class="abs center" style="top:572px;color:#fff;font-size:3px">Supporting arts education for children</div>

  <div class="abs" style="left:23px;top:615px;width:95px;font-size:2.7px;line-height:1.6">
    <p>Art is a vital part of children's education and critical to a community's healing and growth. NOVAworld is honored to announce an ongoing collaboration with LA-based artist Theo Marlow and Ardent &amp; Vale Gallery to support arts education at Haven schools in Mexico and Greece. Beginning in 2021, this project has included donations of art materials to Haven locations, funding to expand our facilities, and visits from trained teaching artists to provide hands-on arts experiences for children.</p>
    <p style="margin-top:4px">Theo Marlow and Ardent &amp; Vale's commitment to bringing arts education to our Havens ensures that all children we serve have a range of opportunities and materials to experience beauty, think in diverse ways, and most importantly, express and rewrite their personal stories.</p>
  </div>
  <div class="abs" style="left:126px;top:615px;width:97px;font-size:2.7px;line-height:1.6">
    <p>NOVAworld and Ardent &amp; Vale's partnership has also brought art education to young artists living in Los Angeles. As part of the Creative Futures LA project, NOVAworld's team worked alongside Theo Marlow and a group of high school students from Downtown Los Angeles to create a visual arts project exploring the global refugee crisis and its humanitarian impact. The culminating presentation and mural were on display to the public at Ardent &amp; Vale Gallery in Downtown Los Angeles in the summer of 2022.</p>
  </div>

  <div class="rule" style="left:23px;top:709px;width:200px"></div>
  <div class="abs center" style="top:717px;font-size:3px;color:var(--gold)">In the News:</div>
  <div class="photo" role="img" aria-label="Students gathered for a group photo in a gallery" style="left:28px;top:728px;width:89px;height:48px;background:linear-gradient(120deg,#5c4c42,#9c8674 50%,#4e433c)"></div>
  <div class="photo" role="img" aria-label="Students painting a mural on a white wall" style="left:129px;top:728px;width:90px;height:48px;background:linear-gradient(120deg,#e8e2d6,#c8a48a 55%,#d9d2c6)"></div>
  <div class="abs" style="left:28px;top:781px;width:92px;font-size:2.5px;line-height:1.5"><div>June 2022, Gallery Weekly</div><div style="margin-top:2px">In Los Angeles, Artist Theo Marlow Launches a New Collaboration with Local High School Arts Students</div><div class="navy" style="margin-top:3px">Read more →</div></div>
  <div class="abs" style="left:129px;top:781px;width:92px;font-size:2.5px;line-height:1.5"><div>July 2021 Ardent &amp; Vale Gallery</div><div style="margin-top:2px">Theo Marlow Press Release: Creative Futures studio at Ardent &amp; Vale launches a year-long collaboration with NOVAworld.</div><div class="navy" style="margin-top:3px">Read more →</div></div>

  <div class="rule" style="left:23px;top:820px;width:200px"></div>
  <h3 class="abs center" style="top:833px;font-size:5.6px;font-weight:500;color:var(--gold)">Westmont University School of Education</h3>
  <div class="abs center" style="top:842px;padding:0 45px;font-size:3.1px;line-height:1.5">NOVAworld and Westmont University co-develop global citizenship education course</div>
  <div class="abs" style="left:23px;top:864px;width:95px;font-size:2.7px;line-height:1.6">
    <p>NOVAworld is proud to partner with the Westmont University School of Education – an institution with a longstanding commitment to dismantling oppressive paradigms in pursuit of equity in education. Our collaboration creates opportunities for students to explore the implications global forced migration has on the future of education as they gain firsthand experience working for NOVAworld – an organization that provides education for asylum seeking, refugee, and (im)migrant children and families.</p>
    <p style="margin-top:4px">In Education for a Shared World, a course co-developed by NOVAworld and Adrian Vell, Associate Director of Undergraduate Programs for Community Engagement, students complete 40-50 hours of service through NOVAworld.</p>
  </div>
  <div class="abs" style="left:126px;top:864px;width:97px;font-size:2.7px;line-height:1.6">
    <p>Participants work directly with Haven educators and NOVAworld leadership to co-develop curricula and programs, conduct research and data collection, and engage in dialogue and cultural exchanges with refugee/asylum seeking and migrant children and families.</p>
    <p style="margin-top:4px">In addition to this course offering, students majoring in Education and Social Transformation have the opportunity to deepen their experiential learning through an 80+ hour academic internship with NOVAworld, offered quarterly to 2-3 undergraduates.</p>
    <p style="margin-top:4px">Education can change the world, and the students of the School of Education are the change-makers who will go on to reshape the landscape of education. We are proud to partner with them as together we create a vision for education that centers global citizenship, social justice, and access for all.</p>
  </div>

  <div class="photo" role="img" aria-label="Smiling child in soft dark light" style="left:0;top:980px;width:245px;height:60px;background:linear-gradient(110deg,#2a2b33,#4a4a52 55%,#2b2d35)"></div>
  <h3 class="abs center" style="top:993px;font-size:6.6px;font-weight:400;color:#fff">Take Action</h3>
  <div class="abs center" style="top:1011px;display:flex;justify-content:center;gap:5px">
    <span class="pill pill-gold" style="font-size:2.5px;width:36px;height:11px">♡ Donate</span>
    <span class="pill pill-navy" style="font-size:2.5px;width:36px;height:11px">Partner with us</span>
    <span class="pill pill-navy" style="font-size:2.5px;width:36px;height:11px">Volunteer with us</span>
  </div>

  <h4 class="abs" style="left:17px;top:1050px;font-size:5.2px;font-weight:500">Sign up for email</h4>
  <div class="field" style="left:17px;top:1062px;width:38px;font-size:2.2px">First name</div>
  <div class="field" style="left:59px;top:1062px;width:38px;font-size:2.2px">Last name</div>
  <div class="field" style="left:17px;top:1071px;width:80px;font-size:2.2px">Email address</div>
  <span class="abs pill pill-gold" style="left:17px;top:1085px;font-size:2.4px;width:24px;height:8px">Submit</span>
  <div class="abs addr" style="left:119px;top:1050px;font-size:2.5px"><b>NOVAworld</b><br>412 Linden Crest, Suite 18<br>Harbor View, California 90000<br>+1 555.010.4421<br>info@novaworld.org<br>EIN# 00-0000000</div>
  <div class="abs" style="left:185px;top:1050px;font-size:2.6px;font-weight:600">Connect with us</div>
  <svg class="abs" style="left:185px;top:1057px" width="24" height="5" viewBox="0 0 24 5"><circle cx="2.5" cy="2.5" r="2" fill="#2e2e2e"/><circle cx="8.5" cy="2.5" r="2" fill="#2e2e2e"/><circle cx="14.5" cy="2.5" r="2" fill="#2e2e2e"/><circle cx="20.5" cy="2.5" r="2" fill="#2e2e2e"/></svg>
</section>

<!-- ===================== WHY ===================== -->
<section class="page" style="left:702px;top:88px;width:311px;height:1078px">
  <div class="photo" role="img" aria-label="Close-up of a child's hands holding colored pencils" style="left:0;top:0;width:311px;height:152px;background:linear-gradient(120deg,#6a4e3c,#a67e5e 45%,#4e5f7a 80%,#6e5a48)"></div>
  <div class="shade" style="height:152px;bottom:auto;background:rgba(30,25,35,.35)"></div>
  <nav class="nav" style="top:6px;padding:0 28px;height:12px">
    <div class="logo" style="font-size:8px"><span class="logo-mark"></span>NOVA</div>
    <div class="nav-links" style="font-size:2.9px;gap:6px;margin-left:20px">
      <span>Home</span><span>Who we are</span><span>Partners &amp; Funders</span><span>Our works</span><span>Get involved</span>
    </div>
    <span class="pill pill-gold" style="margin-left:auto;font-size:2.9px;width:31px;height:10px">DONATE</span>
  </nav>
  <h1 class="hero-title" style="top:52px;font-size:17px">Why NOVAworld?</h1>
  <p class="abs center" style="top:88px;padding:0 70px;font-size:6.4px;line-height:1.8;color:#fff">NOVAworld's work addresses a global unmet need: early childhood education for the world's most vulnerable children.</p>

  <h3 class="abs center" style="top:168px;font-size:6.6px;font-weight:500">Did you know…</h3>
  <svg class="abs" style="left:23px;top:188px" width="20" height="20" viewBox="0 0 20 20"><circle cx="10" cy="10" r="9" fill="none" stroke="#c39c5e" stroke-width="2"/><circle cx="10" cy="8" r="2.5" fill="#213a8a"/><rect x="7" y="11" width="6" height="4" rx="1.5" fill="#213a8a"/></svg>
  <div class="abs stat-num" style="left:26px;top:209px;font-size:6px">8M</div>
  <p class="abs" style="left:47px;top:191px;width:56px;font-size:3px;line-height:1.45">There are 8M million refugee children around the world who do not have access to education?</p>
  <svg class="abs" style="left:116px;top:188px" width="18" height="18" viewBox="0 0 18 18"><circle cx="9" cy="9" r="7.5" fill="#c39c5e"/><path d="M5 7c2-2 6-2 8 0M5 11c2 2 6 2 8 0M9 3v12" stroke="#fff" stroke-width=".8" fill="none"/></svg>
  <div class="abs stat-num" style="left:116px;top:208px;font-size:6px">90%</div>
  <p class="abs" style="left:136px;top:191px;width:56px;font-size:3px;line-height:1.45">of brain development happens between the ages of 0-5 years old?</p>
  <svg class="abs" style="left:202px;top:189px" width="19" height="19" viewBox="0 0 19 19"><circle cx="9.5" cy="9.5" r="8" fill="none" stroke="#e3e3e3" stroke-width="1.6"/><path d="M9.5 1.5a8 8 0 0 1 6 2.7" stroke="#c39c5e" stroke-width="1.6" fill="none"/><text x="9.5" y="11.3" font-size="5" text-anchor="middle" fill="#213a8a" font-family="Poppins, sans-serif">2%</text></svg>
  <p class="abs" style="left:226px;top:193px;width:60px;font-size:3px;line-height:1.45">Less than 2% of all humanitarian aid goes to education?</p>

  <h3 class="abs" style="left:25px;top:250px;font-size:7.6px;font-weight:500">And yet…</h3>
  <p class="abs" style="left:25px;top:270px;width:120px;font-size:3.4px;line-height:1.65">Time and again, research shows that high quality early childhood education is one of the best investments a society can make, not just for the positive impact on the individual child, but for the meaningful long-term, socio-economic impact it has on the entire community.</p>
  <p class="abs" style="left:25px;top:334px;width:120px;font-size:3.4px;line-height:1.65">A recent international policy brief on early childhood programs as a pathway to sustainability in times of global uncertainty stresses that now more than ever, investing in sustainable, flexible high-quality early childhood education programs is imperative for the long-term economic and geopolitical health of communities around the globe.</p>
  <div class="photo" role="img" aria-label="Children drawing with pencils at a table" style="left:163px;top:248px;width:122px;height:146px;background:linear-gradient(150deg,#d8cfc2,#b58f72 45%,#e6e0d8 75%,#8c7a6a)"></div>

  <div class="abs" style="left:0;top:420px;width:311px;height:127px;background:var(--gold)"></div>
  <p class="abs center" style="top:447px;padding:0 60px;font-size:8px;line-height:1.6;color:#fff;font-weight:300">NOVAworld has created a scalable, sustainable and responsive model for bringing low-cost, high quality early childhood education where it's most needed.</p>
  <div class="abs center" style="top:516px;font-size:3.4px;color:#fff">Learn more about the Haven model →</div>

  <h3 class="abs center" style="top:560px;font-size:6.6px;font-weight:500">Our Impact</h3>
  <div class="abs center" style="top:573px;font-size:4px">NOVAworld by the numbers</div>

  <div class="abs" style="left:48px;top:600px;width:100px">
    <div class="stat-num" style="font-size:6.2px"><span style="color:var(--gold)">▣</span> 100,000+</div>
    <div class="stat-label" style="font-size:3.4px">hours of education provided to children</div>
  </div>
  <div class="abs" style="left:48px;top:621px;width:100px">
    <div class="stat-num" style="font-size:6.2px"><span style="color:var(--gold)">♟</span> Over 5,000</div>
    <div class="stat-label" style="font-size:3.4px;margin-top:4px">children and families enrolled</div>
  </div>
  <div class="abs" style="left:48px;top:645px;width:100px">
    <div class="stat-num" style="font-size:6.2px"><span style="color:var(--gold)">▤</span> 17 Classroom</div>
    <div class="stat-label" style="font-size:3.4px;margin-top:4px">in 4 countries, spanning 3 continents</div>
  </div>
  <div class="abs" style="left:48px;top:671px;width:100px">
    <div class="stat-num" style="font-size:6.2px"><span style="color:var(--gold)">▲</span> 43,680 Meals</div>
    <div class="stat-label" style="font-size:3.4px;margin-top:4px">served annually at Haven Congo</div>
  </div>
  <div class="abs" style="left:48px;top:698px;width:90px">
    <div class="stat-num" style="font-size:6.2px"><span style="color:var(--gold)">▥</span> 6 shelters</div>
    <div class="stat-label" style="font-size:3.4px;margin-top:4px">Mobile Haven serves 6 shelters, 4 days a week</div>
  </div>

  <div class="abs" style="left:164px;top:603px;width:110px">
    <div class="stat-num" style="font-size:6.2px"><span style="color:var(--gold)">♟</span> 1,000+</div>
    <div class="stat-label" style="font-size:3.4px">participants in the parenting program</div>
  </div>
  <div class="abs" style="left:164px;top:625px;width:110px">
    <div class="stat-num" style="font-size:6.2px"><span style="color:var(--gold)">■</span> 1,000+</div>
    <div class="stat-label" style="font-size:3.4px;margin-top:2px">children provided with warm clothing, diapers, wipes</div>
  </div>
  <div class="abs" style="left:164px;top:654px;width:110px">
    <div class="stat-num" style="font-size:6.2px"><span style="color:var(--gold)">♥</span> 4,000+</div>
    <div class="stat-label" style="font-size:3.4px;margin-top:2px">supporters committed to NOVAworld's mission</div>
  </div>
  <div class="abs" style="left:164px;top:681px;width:100px">
    <div class="stat-num" style="font-size:6.2px"><span style="color:var(--gold)">♟</span> 500</div>
    <div class="stat-label" style="font-size:3.4px;margin-top:2px">young artists cultivated at Haven Athens &amp; Canyon Haven</div>
  </div>

  <h3 class="abs center" style="top:736px;font-size:6.4px;font-weight:600">2021 GLOBAL REPORT</h3>
  <div class="abs center" style="top:748px;font-size:4px">A brief look at NOVAworld's work</div>
  <div class="photo" role="img" aria-label="Annual report spread with a world map, program photos and staff portraits" style="left:60px;top:763px;width:192px;height:116px;background:linear-gradient(135deg,#3c3c40 0 3%,#f3efe6 3% 97%,#3c3c40 97%)"></div>

  <div class="photo" role="img" aria-label="Smiling child in soft dark light" style="left:0;top:928px;width:311px;height:75px;background:linear-gradient(110deg,#2a2b33,#4a4a52 55%,#2b2d35)"></div>
  <h3 class="abs center" style="top:944px;font-size:8px;font-weight:400;color:#fff">Take Action</h3>
  <div class="abs center" style="top:968px;display:flex;justify-content:center;gap:6px">
    <span class="pill pill-gold" style="font-size:3px;width:45px;height:14px">♡ Donate</span>
    <span class="pill pill-navy" style="font-size:3px;width:45px;height:14px">Partner with us</span>
    <span class="pill pill-navy" style="font-size:3px;width:45px;height:14px">Volunteer with us</span>
  </div>

  <h4 class="abs" style="left:22px;top:1020px;font-size:6.4px;font-weight:500">Sign up for email</h4>
  <div class="field" style="left:22px;top:1034px;width:48px">First name</div>
  <div class="field" style="left:75px;top:1034px;width:48px">Last name</div>
  <div class="field" style="left:22px;top:1046px;width:101px">Email address</div>
  <span class="abs pill pill-gold" style="left:22px;top:1062px;font-size:3px;width:29px;height:10px">Submit</span>
  <div class="abs addr" style="left:152px;top:1021px"><b>NOVAworld</b><br>412 Linden Crest, Suite 18<br>Harbor View, California 90000<br>+1 555.010.4421<br>info@novaworld.org<br>EIN# 00-0000000</div>
</section>

</body>
</html>
```